Social Media Overlay for Ormond Real Estate

We need an social media overlay that can be added to a photo of a house that includes our current logo and a call to action of "Just Listed". This needs to be something that we can use for every new house that we list. Attached is our current logo in both company colors, purple and white. An example of a overlay from Plazeo that we like.

Target Market(s)

Social Media Real Estate Community - Real Estate Agents, Brokers, Buyers & Sellers

Industry/Entity Type

Real Estate

Font styles to use
Sans Serif

Colors
6c459b

Requirements
Must have
• the company colors, purple and white and the company logo
Nice to have
• call to action "Just Listed"
• some layered, texture, or 3-D effect
Should not have
• Should be clean and simple; nothing too busy

```html
<!DOCTYPE html>
<html lang="en">
<head>
<meta charset="utf-8">
<title>Ormond Real Estate – Just Listed Overlays</title>
<link rel="stylesheet" href="https://fonts.googleapis.com/css2?family=Barlow:wght@400;500&display=swap">
<style>
  :root {
    --violet-bright: #6a00c4;
    --violet-mid: #6418a8;
    --violet-deep: #5c2d82;
    --brand-purple: #6c459b;
    --white: #ffffff;
    --page: #ffffff;
  }
  html, body {
    margin: 0;
    padding: 0;
    width: 1200px;
    height: 1200px;
    overflow: hidden;
    background: var(--page);
  }
  .overlay-sheet {
    display: block;
    width: 1200px;
    height: 1200px;
  }
  .cta-text {
    font-family: "Barlow", "Helvetica Neue", Arial, sans-serif;
    font-weight: 500;
    fill: var(--white);
  }
  .brand-name,
  .brand-tagline {
    font-family: "Barlow", "Helvetica Neue", Arial, sans-serif;
    font-weight: 400;
    fill: var(--white);
  }
  .divider { stroke: var(--white); stroke-width: 4; }
  .hang-hole { fill: var(--white); }
</style>
</head>
<body>
<svg class="overlay-sheet" viewBox="0 0 1920 1920" xmlns="http://www.w3.org/2000/svg" aria-label="Four Just Listed overlay variations for Ormond Real Estate">
  <defs>
    <linearGradient id="fade-tab" x1="498" y1="0" x2="542" y2="0" gradientUnits="userSpaceOnUse">
      <stop offset="0" stop-color="var(--violet-bright)"/>
      <stop offset="1" stop-color="var(--violet-deep)"/>
    </linearGradient>
    <linearGradient id="fade-bookmark" x1="526" y1="0" x2="732" y2="0" gradientUnits="userSpaceOnUse">
      <stop offset="0" stop-color="var(--violet-bright)"/>
      <stop offset="1" stop-color="var(--violet-deep)"/>
    </linearGradient>
    <linearGradient id="fade-ribbon" x1="732" y1="0" x2="1427" y2="0" gradientUnits="userSpaceOnUse">
      <stop offset="0" stop-color="var(--violet-bright)"/>
      <stop offset="0.75" stop-color="var(--violet-deep)"/>
      <stop offset="1" stop-color="var(--violet-deep)"/>
    </linearGradient>
    <linearGradient id="fade-flag" x1="460" y1="0" x2="1466" y2="0" gradientUnits="userSpaceOnUse">
      <stop offset="0" stop-color="var(--violet-bright)"/>
      <stop offset="0.25" stop-color="var(--violet-bright)"/>
      <stop offset="0.75" stop-color="var(--violet-deep)"/>
      <stop offset="1" stop-color="var(--violet-deep)"/>
    </linearGradient>
    <linearGradient id="fade-tag" x1="652" y1="0" x2="1273" y2="0" gradientUnits="userSpaceOnUse">
      <stop offset="0" stop-color="var(--violet-bright)"/>
      <stop offset="0.7" stop-color="var(--violet-deep)"/>
      <stop offset="1" stop-color="var(--violet-deep)"/>
    </linearGradient>
    <linearGradient id="fade-header" x1="0" y1="1473" x2="0" y2="1621" gradientUnits="userSpaceOnUse">
      <stop offset="0" stop-color="var(--violet-bright)"/>
      <stop offset="1" stop-color="var(--violet-deep)"/>
    </linearGradient>
    <linearGradient id="fade-pennant" x1="0" y1="1621" x2="0" y2="1798" gradientUnits="userSpaceOnUse">
      <stop offset="0" stop-color="var(--violet-bright)"/>
      <stop offset="1" stop-color="var(--violet-deep)"/>
    </linearGradient>
  </defs>

  <!-- Bookmark ribbon -->
  <g class="overlay bookmark-ribbon">
    <rect class="ribbon-tab" x="498" y="150" width="44" height="212" fill="url(#fade-tab)"/>
    <polygon class="ribbon-band" points="732,150 1427,150 1384,256 1423,362 732,362" fill="url(#fade-ribbon)"/>
    <polygon class="ribbon-bookmark" points="526,131 732,131 732,438 629,379 526,438" fill="url(#fade-bookmark)"/>
    <text class="brand-name" x="629" y="262" font-size="56" text-anchor="middle" textLength="164" lengthAdjust="spacingAndGlyphs">Ormond</text>
    <text class="brand-tagline" x="633" y="290" font-size="30" text-anchor="middle" textLength="148" lengthAdjust="spacingAndGlyphs">Real Estate</text>
    <text class="cta-text" x="745" y="290" font-size="114" textLength="615" lengthAdjust="spacingAndGlyphs">JUST LISTED</text>
  </g>

  <!-- Notched flag -->
  <g class="overlay notched-flag">
    <path class="flag-shape" d="M478,623 H1466 L1381,736 L1466,848 H478 Q460,848 460,830 V641 Q460,623 478,623 Z" fill="url(#fade-flag)"/>
    <text class="cta-text" x="476" y="767" font-size="114" textLength="612" lengthAdjust="spacingAndGlyphs">JUST LISTED</text>
    <line class="divider" x1="1113" y1="650" x2="1113" y2="822"/>
    <text class="brand-name" x="1257" y="746" font-size="80" text-anchor="middle" textLength="210" lengthAdjust="spacingAndGlyphs">Ormond</text>
    <text class="brand-tagline" x="1257" y="785" font-size="40" text-anchor="middle" textLength="194" lengthAdjust="spacingAndGlyphs">Real Estate</text>
  </g>

  <!-- Price-tag -->
  <g class="overlay price-tag">
    <path class="tag-shape" d="M670,1073 H1138 Q1155,1073 1168,1084 L1268,1176 Q1276,1185 1268,1194 L1168,1284 Q1155,1298 1138,1298 H670 Q652,1298 652,1280 V1091 Q652,1073 670,1073 Z" fill="url(#fade-tag)"/>
    <circle class="hang-hole" cx="1214" cy="1186" r="17"/>
    <text class="cta-text" x="668" y="1190" font-size="98" textLength="497" lengthAdjust="spacingAndGlyphs">JUST LISTED</text>
    <text class="brand-name" x="913" y="1262" font-size="64" text-anchor="middle" textLength="160" lengthAdjust="spacingAndGlyphs">Ormond</text>
    <text class="brand-tagline" x="912" y="1291" font-size="30" text-anchor="middle" textLength="148" lengthAdjust="spacingAndGlyphs">Real Estate</text>
  </g>

  <!-- Header with pennant -->
  <g class="overlay header-pennant">
    <polygon class="header-band" points="616,1473 1309,1473 1267,1621 658,1621" fill="url(#fade-header)"/>
    <polygon class="pennant" points="729,1621 1197,1621 1197,1798 963,1763 729,1798" fill="url(#fade-pennant)"/>
    <text class="cta-text" x="682" y="1580" font-size="104" textLength="563" lengthAdjust="spacingAndGlyphs">JUST LISTED</text>
    <text class="brand-name" x="951" y="1697" font-size="72" text-anchor="middle" textLength="172" lengthAdjust="spacingAndGlyphs">Ormond</text>
    <text class="brand-tagline" x="951" y="1728" font-size="34" text-anchor="middle" textLength="158" lengthAdjust="spacingAndGlyphs">Real Estate</text>
  </g>
</svg>
</body>
</html>
```